We need a cover designed for our book on parenting. The focus of this book is on the parents, not on the child! We like the idea of this title having a double meaning - insight as in gaining insights into parenting, and "in sight" as in looking inward as parents and how to improve ourselves rather than looking outward to improve our children. We would love for the cover to somehow represent this double meaning. I can upload an excerpt from the book soon over the next few days.
Updates

Reason: We are still reviewing the amazing designs! Thank you so much! :)

Target Market(s)

Parents with kids of any age from babies through adult children.

Requirements
Must have
• Title is: Harbor Parenting
• Subtitle is: Raising Families Through Reflection
• Authors names: Lena Morrow, LCSW Daniel Morrow, Ph.D.

```html
<!DOCTYPE html>
<html lang="en">
<head>
<meta charset="UTF-8">
<title>Harbor Parenting — Book Cover</title>
<link href="https://fonts.googleapis.com/css2?family=Oswald:wght@400;500&family=Roboto:wght@400;700&display=swap" rel="stylesheet">
<style>
  :root {
    --page-bg: #e6e6e6;
    --cover-bg: #f7f7f7;
    --title-green: #2f6b5c;
    --title-purple: #8c6791;
    --band-green: #346e5f;
    --band-text: #ffffff;
    --figure-purple: #b9a1bd;
    --figure-green: #93b5ab;
  }
  html, body {
    margin: 0;
    padding: 0;
    width: 1200px;
    height: 900px;
    overflow: hidden;
    background: var(--page-bg);
  }
  .canvas {
    position: relative;
    width: 1200px;
    height: 900px;
  }
  .book-cover {
    position: absolute;
    left: 370px;
    top: 20px;
    width: 460px;
    height: 860px;
    background: var(--cover-bg);
    box-shadow: 0 2px 10px rgba(0,0,0,0.12);
    overflow: hidden;
  }
  .title-art {
    position: absolute;
    left: 0;
    top: 0;
    width: 460px;
    height: 380px;
  }
  .title-line {
    font-family: "Oswald", sans-serif;
    font-weight: 500;
  }
  .title-main { fill: var(--title-green); }
  .title-sub { fill: var(--title-purple); }
  .family-figures {
    position: absolute;
    left: 58px;
    top: 410px;
    width: 336px;
    height: 325px;
    border-radius: 160px 160px 6px 6px;
    background: linear-gradient(90deg, var(--figure-purple) 0%, #d9cddb 48%, #c7dbd5 52%, var(--figure-green) 100%);
    opacity: 0.55;
  }
  .subtitle {
    position: absolute;
    left: 0;
    width: 460px;
    top: 605px;
    margin: 0;
    text-align: center;
    font-family: "Oswald", sans-serif;
    font-weight: 400;
    font-size: 29px;
    line-height: 1.22;
    color: var(--title-purple);
    text-transform: uppercase;
  }
  .subtitle span { display: block; }
  .author-band {
    position: absolute;
    left: 0;
    bottom: 0;
    width: 460px;
    height: 94px;
    background: var(--band-green);
    display: flex;
    align-items: center;
    justify-content: center;
    font-family: "Roboto", sans-serif;
    color: var(--band-text);
    white-space: nowrap;
  }
  .author-name {
    font-weight: 700;
    font-size: 20px;
    text-transform: uppercase;
  }
  .author-credential {
    font-weight: 400;
    font-size: 12px;
    margin-right: 6px;
  }
  .author-join {
    font-weight: 400;
    font-size: 20px;
    margin-right: 6px;
  }
</style>
</head>
<body>
  <main class="canvas">
    <article class="book-cover">
      <svg class="title-art" viewBox="0 0 460 380" aria-label="Harbor Parenting">
        <text class="title-line title-main" x="40" y="208" font-size="230" textLength="380" lengthAdjust="spacingAndGlyphs">HARBOR</text>
        <text class="title-line title-sub" x="40" y="365" font-size="170" textLength="380" lengthAdjust="spacingAndGlyphs">PARENTING</text>
      </svg>

      <div class="family-figures" role="img" aria-label="Simple outline figures of two parents side by side, one purple and one green"></div>

      <h2 class="subtitle">
        <span>Raising</span>
        <span>Families Through</span>
        <span>Reflection</span>
      </h2>

      <footer class="author-band">
        <span class="author-name">Lena Morrow</span><span class="author-credential">, LCSW</span>
        <span class="author-join">&amp;</span>
        <span class="author-name">Daniel Morrow</span><span class="author-credential">, Ph.D.</span>
      </footer>
    </article>
  </main>
</body>
</html>
```